St. Paddy’s Day Invitation

Invitation to text to people:
6th Annual St. Paddy’s Day Party
Where: The Kelterbrook’s
When: Saturday, March 25
Acoustic session by Taddeo Lindqvist from Mr. Pocketwatch
Fundraiser for Milo Ferreday ‘Open Harbor’ Fund

Target Market(s)

Adults only, all friends from our town, Moorestown, NJ

Colors
00AB8E
00BBA5
67D7C9
C6EFE9
E9F9F6
59FF00
82FF00
B8FF75
E3FFCB
F4FFEA

```html
<!DOCTYPE html>
<html lang="en">
<head>
<meta charset="utf-8">
<title>6th Annual St. Paddy’s Day Party</title>
<link href="https://fonts.googleapis.com/css2?family=Uncial+Antiqua&family=Poppins:wght@300;400;700&display=swap" rel="stylesheet">
<style>
  :root {
    --green-deep: #0c5a1a;
    --green-mid: #1f8a2a;
    --green-light: #3aa83a;
    --yellow: #e6f01f;
    --white: #ffffff;
    --photo-dark: #1c1c1c;
    --photo-mid: #6a6a6a;
  }
  * { margin: 0; padding: 0; box-sizing: border-box; }
  html, body { width: 857px; height: 1200px; overflow: hidden; }
  body { background: var(--green-deep); }
  .invitation {
    position: relative;
    width: 857px;
    height: 1200px;
    overflow: hidden;
    font-family: "Poppins", sans-serif;
    color: var(--white);
  }
  .backdrop {
    position: absolute; inset: 0;
    background: radial-gradient(ellipse at 50% 45%, var(--green-light) 0%, var(--green-mid) 45%, var(--green-deep) 100%);
  }
  .title {
    position: absolute; left: 0; top: 0; width: 100%;
    font-family: "Uncial Antiqua", serif;
    color: var(--yellow);
  }
  .title-number {
    position: absolute; left: 128px; top: 78px;
    font-size: 250px; line-height: 1;
  }
  .title-line {
    position: absolute; left: 324px;
    font-size: 52px; line-height: 1; white-space: nowrap;
  }
  .title-line.first { top: 88px; }
  .title-line.second { top: 166px; left: 328px; }
  .title-line.third { top: 244px; left: 328px; }
  .title-line sup { font-size: 40px; vertical-align: 0; margin-right: 14px; }
  .detail {
    position: absolute; top: 392px; width: 380px;
    text-align: center;
  }
  .detail.where { left: 24px; }
  .detail.when { left: 436px; }
  .detail-label { font-weight: 300; font-size: 27px; letter-spacing: 1px; line-height: 1.2; }
  .detail-value { margin-top: 16px; font-weight: 700; font-size: 37px; line-height: 1.4; color: var(--yellow); }
  .divider {
    position: absolute; left: 427px; top: 390px;
    width: 2px; height: 174px; background: var(--yellow);
  }
  .photo { position: absolute; }
  .photo.singer {
    left: 0; top: 588px; width: 444px; height: 612px;
    border-radius: 200px 220px 0 0;
    background: linear-gradient(160deg, var(--photo-mid) 0%, var(--photo-dark) 60%);
  }
  .photo.child {
    left: 672px; top: 600px; width: 185px; height: 600px;
    border-radius: 90px 0 0 0;
    background: linear-gradient(180deg, #b99a86 0%, #9a9a9a 40%, #4a4a4a 100%);
  }
  .fund-mark {
    position: absolute; left: 498px; top: 838px;
    width: 276px; text-align: center;
    display: flex; align-items: center; justify-content: center; gap: 10px;
    font-weight: 700; font-size: 28px; color: var(--white);
  }
  .fund-mark .dot { width: 18px; height: 18px; border-radius: 50%; background: var(--white); flex: none; }
  .caption {
    position: absolute; top: 980px; width: 420px;
    text-align: center; line-height: 1.2;
  }
  .caption.performer { left: 42px; }
  .caption.cause { left: 432px; }
  .caption-lead { font-weight: 400; font-size: 29px; }
  .caption-name { font-weight: 700; font-size: 38px; color: var(--yellow); line-height: 1.22; }
  .caption-note { font-weight: 400; font-size: 26px; }
</style>
</head>
<body>
<main class="invitation">
  <div class="backdrop" role="img" aria-label="Green background with a faint pattern of shamrocks and horseshoes"></div>

  <h1 class="title">
    <span class="title-number">6</span>
    <span class="title-line first"><sup>th</sup>Annual</span>
    <span class="title-line second">St. Paddy’s</span>
    <span class="title-line third">Day Party</span>
  </h1>

  <section class="detail where">
    <p class="detail-label">where</p>
    <p class="detail-value">The<br>Kelterbrook’s</p>
  </section>
  <div class="divider"></div>
  <section class="detail when">
    <p class="detail-label">when</p>
    <p class="detail-value">Saturday,<br>March 25</p>
  </section>

  <div class="photo singer" role="img" aria-label="Black and white photo of the performer singing into a microphone"></div>
  <div class="photo child" role="img" aria-label="Photo of a smiling boy in a baseball cap and jersey"></div>

  <div class="fund-mark"><span class="dot"></span>Open Harbor Fund</div>

  <section class="caption performer">
    <p class="caption-lead">Acoustic session by</p>
    <p class="caption-name">Taddeo<br>Lindqvist</p>
    <p class="caption-note">from Mr. Pocketwatch</p>
  </section>

  <section class="caption cause">
    <p class="caption-lead">Fundraiser for</p>
    <p class="caption-name">Milo Ferreday<br>‘Open Harbor’<br>Fund</p>
  </section>
</main>
</body>
</html>
```